Tallow Farm Brochure

To design a small brochure that tells people about our U-Pick cherry farm, where we are, when we are open and what our contact details are.

We have existing logo's which should be used. I have uploaded a file with these details.

Details about us are all located on:-
www.friendlink.example/tallowfarm
https://circlepage.example/u/0/b/704916382057419263851/704916382057419263851/about/p/pub

Farm

```html
<!DOCTYPE html>
<html lang="en">
<head>
<meta charset="utf-8">
<title>Tallow Farm Brochure</title>
<link rel="stylesheet" href="https://fonts.googleapis.com/css2?family=Lato:wght@400;700&family=Arvo&display=swap">
<style>
  :root {
    --teal: #2a8a72;
    --teal-dark: #1f6f5c;
    --lime: #9bc43a;
    --lime-light: #b6d85a;
    --leaf-green: #3a9a4e;
    --ink: #1e3d2e;
    --body-grey: #555555;
    --paper: #ffffff;
    --backdrop: #e6e6e4;
  }
  * { box-sizing: border-box; margin: 0; padding: 0; }
  html, body { width: 1200px; height: 626px; overflow: hidden; }
  body { background: var(--backdrop); font-family: "Lato", sans-serif; position: relative; }

  .brochure-spread {
    position: absolute; left: 214px; top: 23px;
    width: 772px; height: 580px;
    background: var(--paper);
    box-shadow: 0 4px 14px rgba(0,0,0,0.18);
    overflow: hidden;
  }
  .spread-art { position: absolute; inset: 0; }

  /* left panel */
  .price-tag {
    position: absolute; left: 0; top: 20px; width: 230px; height: 72px;
    background: linear-gradient(180deg, var(--lime-light), var(--lime));
    border-radius: 0 14px 14px 0;
    padding: 9px 14px 0 28px;
    font-size: 14.5px; line-height: 1.3; color: var(--ink);
  }
  .price-tag .price { color: var(--paper); }
  .about-copy {
    position: absolute; left: 18px; top: 104px; width: 228px;
    font-size: 11px; line-height: 1.38; color: var(--body-grey);
  }
  .about-copy p + p { margin-top: 9px; }
  .varieties-copy {
    position: absolute; left: 14px; top: 446px; width: 232px;
    font-size: 10px; line-height: 13px; color: var(--paper);
  }

  /* middle panel */
  .contact-block {
    position: absolute; left: 290px; top: 124px; width: 210px;
    color: var(--paper); font-size: 14.5px; font-weight: 700; line-height: 1.35;
  }
  .contact-block .address { text-align: center; width: 190px; }
  .contact-line { display: flex; align-items: center; gap: 7px; margin-top: 5px; }
  .contact-line svg { flex: none; }

  /* right panel */
  .farm-name {
    position: absolute; left: 514px; top: 70px; width: 258px;
    text-align: center; color: var(--leaf-green); font-weight: 700; line-height: 0.95;
  }
  .farm-name .first { display: block; font-size: 44px; }
  .farm-name .second { display: block; font-size: 30px; }
  .intro-box {
    position: absolute; left: 532px; top: 442px; width: 240px; height: 108px;
    background: var(--paper); border-radius: 14px 0 0 14px;
    box-shadow: 0 2px 8px rgba(0,0,0,0.2);
    padding: 12px 10px;
    font-family: "Arvo", serif; font-size: 12.5px; line-height: 1.35;
    color: #444; text-align: center;
  }
</style>
</head>
<body>
<main class="brochure-spread">
  <svg class="spread-art" width="772" height="580" viewBox="0 0 772 580">
    <defs>
      <linearGradient id="cherryTone" x1="0" y1="0" x2="1" y2="1">
        <stop offset="0" stop-color="#e34a4a"/>
        <stop offset="0.6" stop-color="#a3121a"/>
        <stop offset="1" stop-color="#f4eeee"/>
      </linearGradient>
      <linearGradient id="orchardTone" x1="0" y1="0" x2="0" y2="1">
        <stop offset="0" stop-color="#c7dcee"/>
        <stop offset="0.3" stop-color="#8fa9b4"/>
        <stop offset="0.42" stop-color="#3f6a3c"/>
        <stop offset="0.6" stop-color="#6fa23a"/>
        <stop offset="1" stop-color="#3f7f24"/>
      </linearGradient>
    </defs>

    <!-- middle panel base -->
    <rect class="middle-panel" x="258" y="0" width="256" height="580" fill="var(--teal)"/>

    <!-- left panel cherry photo -->
    <rect role="img" aria-label="Close-up photo of ripe red cherries with water drops"
          x="0" y="312" width="220" height="160" fill="url(#cherryTone)"/>
    <!-- left panel lower band -->
    <path class="varieties-band" d="M0,432 C90,418 180,414 258,410 L258,580 L0,580 Z" fill="var(--teal)"/>

    <!-- orchard photo across middle and right panels -->
    <path role="img" aria-label="Photo of cherry orchard rows with a dam and distant mountain ranges"
          d="M258,580 L258,570 C300,440 390,345 514,318 C620,295 720,220 772,110 L772,580 Z"
          fill="url(#orchardTone)"/>

    <!-- swooshes: parallel stripes following the photo edge -->
    <path class="swoosh-teal" transform="translate(0,-27)"
          d="M258,570 C300,440 390,345 514,318 C620,295 720,220 772,110"
          fill="none" stroke="var(--teal)" stroke-width="12"/>
    <path class="swoosh-lime" transform="translate(0,-14)"
          d="M258,570 C300,440 390,345 514,318 C620,295 720,220 772,110"
          fill="none" stroke="var(--lime)" stroke-width="8"/>
    <path class="swoosh-white"
          d="M258,570 C300,440 390,345 514,318 C620,295 720,220 772,110"
          fill="none" stroke="var(--paper)" stroke-width="12"/>
  </svg>

  <div class="price-tag">Prices for take away U-Pick fruit is <span class="price">$8</span> per kilo. There are no entry fees.</div>

  <div class="about-copy">
    <p>Visitors are welcome to picnic beside our scenic dam and enjoy the views of the valley, the neighboring vineyards and the distant mountain ranges.</p>
    <p>Cherries have been grown at Tallow Farm for the last 50 or so years. Some of our trees today date back to these original plantings.</p>
    <p>Our cherry trees are pruned to enable easy picking for people of all ages. We have over 4,000 trees which ensures we always have more than plenty of juicy ripe fruit to pick.</p>
  </div>

  <p class="varieties-copy">We have 12 varieties of cherries, most of which are heritage varieties and are rarely found elsewhere. Some have dark, near black fruit, some have bright mahogany sweet highly juicy fruit and others have red firm fruit. Our cherries are known as mid-season cherries and are typically available in November and December, sometimes still available at the beginning of January.</p>

  <div class="contact-block">
    <p class="address">18 Ridgeback Road<br>Tallow, Victoria</p>
    <p class="contact-line">
      <svg width="15" height="15" viewBox="0 0 15 15"><rect width="15" height="15" rx="3" fill="var(--lime)"/><path d="M4.2,3 L6,3 L6.6,5.4 L5.6,6.2 C6.2,7.6 7.4,8.8 8.8,9.4 L9.6,8.4 L12,9 L12,10.8 C12,11.4 11.4,12 10.8,12 C7,11.8 3.2,8 3,4.2 C3,3.6 3.6,3 4.2,3 Z" fill="var(--teal-dark)"/></svg>
      +61 1300 555 014
    </p>
    <p class="contact-line">
      <svg width="15" height="15" viewBox="0 0 15 15"><circle cx="7.5" cy="7.5" r="6.5" fill="none" stroke="var(--lime)" stroke-width="1.4"/><ellipse cx="7.5" cy="7.5" rx="2.8" ry="6.5" fill="none" stroke="var(--lime)" stroke-width="1.1"/><path d="M1,7.5 H14" stroke="var(--lime)" stroke-width="1.1"/></svg>
      www.tallowfarm.example
    </p>
  </div>

  <h1 class="farm-name"><span class="first">Tallow</span><span class="second">Farm</span></h1>

  <p class="intro-box">Tallow Farm is in the beautiful Yarra Valley, an ideal location for growing sweet juicy cherries. Visit us for Pick Your Own or Pre-Picked Cherries.</p>
</main>
</body>
</html>
```